Creative & Appealing Business Card

Required a business card for Ferndale Recoveries
We specialise in claims management services for PPI ( Payment Protection Insurance.
2 sided business card
Round Corners
I like embossed and raised lettering

Industry/Entity Type

Business

```html
<!DOCTYPE html>
<html lang="en">
<head>
<meta charset="utf-8">
<title>Ferndale Recoveries – Business Card</title>
<link rel="stylesheet" href="https://fonts.googleapis.com/css2?family=Josefin+Sans:wght@300;400&family=Roboto:wght@700&family=Ubuntu:wght@300;400&family=PT+Sans+Narrow:wght@400;700&display=swap">
<style>
  :root {
    --page: #e8e6e3;
    --slate: #435560;
    --slate-deep: #2d3b43;
    --paper: #ffffff;
    --ink-light: #ffffff;
    --ink-soft: #a9c3d0;
    --ribbon-text: #b8d0dc;
    --decor: #ececec;
  }
  html, body {
    margin: 0;
    width: 1025px;
    height: 1200px;
    overflow: hidden;
    background: var(--page);
  }
  .card {
    position: absolute;
    left: 46px;
    width: 932px;
    height: 532px;
    background: var(--slate);
    border-radius: 14px;
    overflow: hidden;
    box-shadow: 0 6px 18px rgba(0,0,0,0.22);
  }
  .card--front { top: 40px; }
  .card--back { top: 628px; }

  .card__paper {
    position: absolute;
    inset: 0;
    background: var(--paper);
  }
  .card--front .card__paper { clip-path: polygon(867px 0, 932px 0, 932px 532px, 802px 532px); }
  .card--back .card__paper { clip-path: polygon(703px 0, 932px 0, 932px 532px, 639px 532px); }

  .card__decor {
    position: absolute;
    width: 190px;
    height: 190px;
    border-radius: 50%;
    background: var(--decor);
  }
  .card--front .card__decor { left: 840px; top: 360px; }
  .card--back .card__decor { left: 745px; top: 290px; }

  .brand {
    position: absolute;
    display: flex;
    align-items: center;
    gap: 16px;
    font-family: "Roboto", Arial, sans-serif;
    font-weight: 700;
    font-size: 32px;
    color: var(--ink-light);
    text-shadow: 0 1px 0 rgba(0,0,0,0.35), 0 -1px 0 rgba(255,255,255,0.12);
  }
  .brand__dot {
    width: 58px;
    height: 58px;
    border-radius: 50%;
    background: var(--ink-light);
    box-shadow: 0 1px 2px rgba(0,0,0,0.3);
  }
  .card--front .brand { left: 48px; top: 99px; }
  .card--back .brand { left: 57px; top: 88px; }

  .name-ribbon {
    position: absolute;
    left: 507px;
    top: 65px;
    width: 381px;
    height: 98px;
    background: var(--slate-deep);
    box-shadow: 3px 5px 10px rgba(0,0,0,0.45);
    text-align: center;
    font-family: "Josefin Sans", "Gill Sans", sans-serif;
    font-weight: 300;
  }
  .name-ribbon__name {
    margin-top: 14px;
    font-size: 48px;
    line-height: 1;
    color: var(--ink-light);
    letter-spacing: 1px;
    text-shadow: 0 1px 1px rgba(0,0,0,0.5);
  }
  .name-ribbon__company {
    margin-top: 8px;
    font-size: 20px;
    letter-spacing: 5px;
    color: var(--ink-soft);
  }

  .contacts {
    position: absolute;
    left: 51px;
    top: 318px;
    margin: 0;
    padding: 0;
    list-style: none;
    font-family: "Ubuntu", "Trebuchet MS", sans-serif;
    font-weight: 300;
    font-size: 27px;
    color: var(--ink-light);
    text-shadow: 0 1px 0 rgba(0,0,0,0.35);
  }
  .contacts__item {
    display: flex;
    align-items: center;
    gap: 10px;
    height: 38px;
  }
  .contacts__icon {
    width: 22px;
    height: 24px;
    flex: none;
  }

  .service-ribbon {
    position: absolute;
    left: 99px;
    top: 280px;
    width: 570px;
    height: 72px;
    background: var(--slate-deep);
    box-shadow: 3px 5px 10px rgba(0,0,0,0.45);
    font-family: "PT Sans Narrow", "Arial Narrow", sans-serif;
    font-weight: 700;
    font-size: 32px;
    line-height: 72px;
    color: var(--ribbon-text);
    padding-left: 30px;
    box-sizing: border-box;
    text-shadow: 0 1px 1px rgba(0,0,0,0.5);
  }
  .services {
    position: absolute;
    left: 122px;
    top: 364px;
    margin: 0;
    padding: 0;
    list-style: none;
    font-family: "PT Sans Narrow", "Arial Narrow", sans-serif;
    font-size: 26px;
    color: var(--ink-light);
    text-shadow: 0 1px 0 rgba(0,0,0,0.35);
  }
  .services__item {
    display: flex;
    align-items: center;
    gap: 8px;
    height: 41px;
  }
  .services__tick { width: 28px; height: 26px; flex: none; }
</style>
</head>
<body>

<section class="card card--front" aria-label="Business card front">
  <div class="card__paper"></div>
  <div class="card__decor"></div>

  <div class="brand"><span class="brand__dot"></span>Ferndale Recoveries</div>

  <div class="name-ribbon">
    <div class="name-ribbon__name">DANIEL MARSH</div>
    <div class="name-ribbon__company">FERNDALE RECOVERIES</div>
  </div>

  <ul class="contacts">
    <li class="contacts__item">
      <svg class="contacts__icon" viewBox="0 0 22 24"><path d="M11 2a7 7 0 0 1 7 7c0 5-7 13-7 13S4 14 4 9a7 7 0 0 1 7-7z" fill="#fff"/><circle cx="11" cy="9" r="3" fill="#435560"/></svg>
      48 Alderton Street London N4 2QP
    </li>
    <li class="contacts__item">
      <svg class="contacts__icon" viewBox="0 0 22 24"><rect x="2" y="6" width="18" height="13" fill="none" stroke="#fff" stroke-width="2"/><path d="M2 6l9 7 9-7" fill="none" stroke="#fff" stroke-width="2"/></svg>
      daniel@ferndalerecoveries.com
    </li>
    <li class="contacts__item">
      <svg class="contacts__icon" viewBox="0 0 22 24"><rect x="5" y="2" width="12" height="20" rx="2" fill="none" stroke="#fff" stroke-width="2"/><line x1="9" y1="18" x2="13" y2="18" stroke="#fff" stroke-width="2"/></svg>
      +44 (0) 333 014 5521
    </li>
    <li class="contacts__item">
      <svg class="contacts__icon" viewBox="0 0 22 24"><rect x="6" y="4" width="10" height="6" fill="#fff"/><rect x="2" y="10" width="18" height="8" rx="1" fill="#fff"/><rect x="6" y="15" width="10" height="5" fill="#435560" stroke="#fff" stroke-width="1.5"/></svg>
      +44 (0) 203 481 6634
    </li>
    <li class="contacts__item">
      <svg class="contacts__icon" viewBox="0 0 22 24"><circle cx="11" cy="12" r="4" fill="none" stroke="#fff" stroke-width="2"/><path d="M15 12v2a3 3 0 0 0 5-1A9 9 0 1 0 15 20" fill="none" stroke="#fff" stroke-width="2"/></svg>
      www.ferndalerecoveries.com
    </li>
  </ul>
</section>

<section class="card card--back" aria-label="Business card back">
  <div class="card__paper"></div>
  <div class="card__decor"></div>

  <div class="brand"><span class="brand__dot"></span>Ferndale Recoveries</div>

  <div class="service-ribbon">Claims Management Service for mis-sold</div>

  <ul class="services">
    <li class="services__item">
      <svg class="services__tick" viewBox="0 0 28 26"><path d="M2 14l8 8L26 3" fill="none" stroke="#fff" stroke-width="4" stroke-linecap="round" stroke-linejoin="round"/></svg>
      Payment Protection Insurance Claims
    </li>
    <li class="services__item">
      <svg class="services__tick" viewBox="0 0 28 26"><path d="M2 14l8 8L26 3" fill="none" stroke="#fff" stroke-width="4" stroke-linecap="round" stroke-linejoin="round"/></svg>
      Interest Rate Hedging Products / SWAPS
    </li>
  </ul>
</section>

</body>
</html>
```